2019 CD Cover Design - Drifting Past Noon

Please Use Uploaded Photo. Feel free to crop and otherwise edit the photo to enrich the design. Title is "Drifting Past Noon" and should be relative prominent in the cover. Artist names are "Marcus Pellham and Rosalind Quaye" and should also be printed on the cover. Please ensure compliance with DiscHarbor Published Requirements, ie CMYK, 300dpi, etc. Planning on giving winner the Back Cover and Inside designs.

Target Market(s)

The album is a set of cover love songs, all duets, many are contemporary country, ie in the style of Copper Wagonwheel, Greta Voss, Harlow Junction. Feel free to innovate!

Industry/Entity Type

Music Download

Colors

Designer to choose colors to be used in the design.

Requirements
Nice to have
• Optional - Third Line of Text - “Contemporary Country Duets”
Should not have
• Please do NOT cut out and completely replace the grassy field background. The CD liner notes will discuss the photo, which is a renowned national park in our hometown.

```html
<!DOCTYPE html>
<html lang="en">
<head>
<meta charset="utf-8">
<title>Drifting Past Noon – CD Cover</title>
<link href="https://fonts.googleapis.com/css2?family=Oswald:wght@600&family=Open+Sans:wght@700&family=Playfair+Display:ital,wght@1,600&family=Great+Vibes&display=swap" rel="stylesheet">
<style>
  :root {
    --canvas: #eeeeee;
    --title-red: #b3151b;
    --ink: #1c1a17;
    --name-white: #ffffff;
    --field-gold: #d8b357;
    --field-amber: #c99a3c;
    --field-green: #8f9a4a;
    --field-light: #e6cd86;
    --badge-gold: #b78630;
    --badge-dark: #8a5d1c;
  }
  * { margin: 0; padding: 0; box-sizing: border-box; }
  html, body { width: 1200px; height: 1200px; overflow: hidden; }
  body {
    background: radial-gradient(circle at 50% 45%, #fafafa 0%, var(--canvas) 75%);
    position: relative;
  }
  .cover {
    position: absolute;
    width: 560px;
    height: 560px;
    overflow: hidden;
    box-shadow: 0 6px 18px rgba(0,0,0,0.18);
  }
  .cover--front { left: 30px; top: 320px; }
  .cover--back { left: 610px; top: 320px; }

  .field-photo {
    position: absolute;
    inset: 0;
    background:
      radial-gradient(ellipse at 80% 30%, rgba(230,205,134,0.7) 0%, transparent 55%),
      linear-gradient(180deg, var(--field-light) 0%, var(--field-gold) 40%, var(--field-amber) 75%, var(--field-green) 100%);
  }
  .field-photo--back {
    background:
      radial-gradient(ellipse at 75% 60%, rgba(143,154,74,0.55) 0%, transparent 50%),
      linear-gradient(180deg, var(--field-light) 0%, var(--field-gold) 45%, var(--field-amber) 80%, var(--field-green) 100%);
  }
  .duo-photo {
    position: absolute;
    left: 0;
    bottom: 0;
    width: 400px;
    height: 500px;
    background: linear-gradient(180deg, rgba(120,110,100,0.25) 0%, rgba(60,60,70,0.55) 60%, rgba(25,25,30,0.75) 100%);
    border-top-right-radius: 160px;
  }

  .tagline {
    position: absolute;
    top: 33px;
    left: 96px;
    font-family: "Open Sans", sans-serif;
    font-weight: 700;
    font-size: 15px;
    letter-spacing: 4.2px;
    color: var(--ink);
    white-space: nowrap;
  }
  .title-stack {
    position: absolute;
    right: 24px;
    top: 118px;
    width: 200px;
    text-align: center;
    font-family: "Oswald", sans-serif;
    font-weight: 600;
    color: var(--title-red);
    font-size: 50px;
    line-height: 72px;
    text-transform: uppercase;
    white-space: nowrap;
  }
  .artists {
    position: absolute;
    right: 40px;
    bottom: 32px;
    text-align: right;
    font-family: "Playfair Display", serif;
    font-style: italic;
    font-weight: 600;
    font-size: 34px;
    line-height: 38px;
    color: var(--name-white);
    text-shadow: 1px 1px 2px rgba(0,0,0,0.7);
    white-space: nowrap;
  }
  .artists__amp { font-size: 24px; margin-right: 4px; }

  .back-title {
    position: absolute;
    top: 44px;
    left: 120px;
    font-family: "Oswald", sans-serif;
    font-weight: 600;
    font-size: 46px;
    line-height: 60px;
    color: var(--title-red);
    text-transform: uppercase;
    letter-spacing: 0.5px;
    white-space: nowrap;
  }
  .tracklist {
    position: absolute;
    top: 140px;
    left: 110px;
    list-style: none;
  }
  .track {
    display: flex;
    align-items: center;
    height: 37px;
  }
  .track__num {
    width: 32px;
    height: 32px;
    border-radius: 50%;
    background: radial-gradient(circle at 40% 35%, var(--badge-gold), var(--badge-dark));
    font-family: "Oswald", sans-serif;
    font-weight: 600;
    font-size: 17px;
    color: var(--ink);
    display: flex;
    align-items: center;
    justify-content: center;
    margin-right: 12px;
  }
  .track__name {
    font-family: "Great Vibes", cursive;
    font-size: 27px;
    color: var(--ink);
    white-space: nowrap;
  }
</style>
</head>
<body>
  <section class="cover cover--front">
    <div class="field-photo" role="img" aria-label="Sunlit golden grass field in a national park"></div>
    <div class="duo-photo" role="img" aria-label="Photo of the two duet singers posed together in the field"></div>
    <p class="tagline">Contemporary Country Duets</p>
    <h1 class="title-stack">Drifting<br>Past<br>Noon</h1>
    <p class="artists">Marcus<br>Pellham<br><span class="artists__amp">&amp;</span>Rosalind<br>Quaye</p>
  </section>

  <section class="cover cover--back">
    <div class="field-photo field-photo--back" role="img" aria-label="Close view of tall golden grass with purple thistle flowers"></div>
    <h2 class="back-title">Drifting Past Noon</h2>
    <ol class="tracklist">
      <li class="track"><span class="track__num">1.</span><span class="track__name">Track Name one</span></li>
      <li class="track"><span class="track__num">2.</span><span class="track__name">Name track two</span></li>
      <li class="track"><span class="track__num">3.</span><span class="track__name">Track name three</span></li>
      <li class="track"><span class="track__num">4.</span><span class="track__name">Name track four</span></li>
      <li class="track"><span class="track__num">5.</span><span class="track__name">Track name five</span></li>
      <li class="track"><span class="track__num">6.</span><span class="track__name">Name track six</span></li>
      <li class="track"><span class="track__num">7.</span><span class="track__name">Track name seven</span></li>
      <li class="track"><span class="track__num">8.</span><span class="track__name">Name track eight</span></li>
      <li class="track"><span class="track__num">9.</span><span class="track__name">Track name nine</span></li>
      <li class="track"><span class="track__num">10.</span><span class="track__name">Name track ten</span></li>
    </ol>
  </section>
</body>
</html>
```